Luxury Business Card Design for High-End Window Treatments

Gilded Vantages
Custom Plantation Shutters & Architectural Shading Systems

⸻

BACK

Daniel Forsythe
Owner

Custom Interior & Exterior Window Treatments

919-482-7034
gildedvantages.com

I have included a picture that I’m hoping we can use on the back, but I’m also wondering if you can get rid of the ladder? Should we get rid of shutters , shades and blinds underneath Gilded Vantages?

Target Market(s)

High-end residential homeowners, custom home builders, architects, interior designers, and luxury renovation clients seeking premium plantation shutters and motorized architectural shading systems.

Industry/Entity Type

Custom Window treatments

Contact Information for Business Card

Front Gilded Vantages Custom Plantation Shutters Motorized Architectural Shading Systems BACK Daniel Forsythe Owner 919-482-7034 GildedVantages.com Custom Interior & Exterior Window Treatments By Appointment

Requirements
Nice to have
• Not 100% sure on nice to halves or the color but you can definitely check out my website to get a better understanding of what I’m trying to do

```html
<!DOCTYPE html>
<html lang="en">
<head>
<meta charset="UTF-8">
<title>Gilded Vantages – Business Card</title>
<link rel="stylesheet" href="https://fonts.googleapis.com/css2?family=Montserrat:wght@400;500;700&family=Raleway:wght@400&display=swap">
<style>
  :root {
    --backdrop: #3a3b3d;
    --card-dark: #25272b;
    --card-dark-edge: #33363b;
    --gold-deep: #8a6a2e;
    --gold: #b8954a;
    --gold-light: #dcc06e;
    --text-light: #ffffff;
    --photo-sky: #8fb4dc;
    --photo-house: #5e6470;
    --photo-green: #4d5a3a;
  }
  * { margin: 0; padding: 0; box-sizing: border-box; }
  html, body { width: 1200px; height: 758px; overflow: hidden; }
  body {
    background: var(--backdrop);
    font-family: "Montserrat", Arial, sans-serif;
    position: relative;
  }
  .card {
    position: absolute;
    top: 216px;
    width: 570px;
    height: 326px;
    border-radius: 18px;
    overflow: hidden;
    background: linear-gradient(135deg, var(--card-dark-edge), var(--card-dark) 55%);
    box-shadow: 0 14px 30px rgba(0,0,0,.45);
  }
  .card-front { left: 20px; }
  .card-back { left: 610px; }
  .card svg { position: absolute; inset: 0; }

  .brand-name {
    font-family: "Raleway", Arial, sans-serif;
    font-weight: 400;
    color: var(--gold);
    line-height: 1.05;
  }
  .card-front .brand-name {
    position: absolute;
    left: 0; right: 0; top: 104px;
    text-align: center;
    font-size: 56px;
  }
  .card-back .brand-name {
    position: absolute;
    left: 332px; width: 230px; top: 28px;
    text-align: center;
    font-size: 30px;
  }
  .name-band {
    position: absolute;
    left: 340px; width: 218px; top: 114px;
    color: var(--text-light);
    text-align: right;
  }
  .person-name { font-weight: 700; font-size: 24px; letter-spacing: .2px; }
  .person-role { font-weight: 500; font-size: 12px; margin-top: 1px; }
  .tagline {
    position: absolute;
    left: 330px; width: 232px; top: 196px;
    color: var(--text-light);
    font-weight: 500;
    font-size: 12.5px;
    line-height: 1.35;
    text-align: center;
  }
  .contact {
    position: absolute;
    right: 18px; top: 250px;
    color: var(--text-light);
    font-size: 12.5px;
    line-height: 1.7;
    text-align: right;
  }
  .contact-line { display: flex; align-items: center; justify-content: flex-end; gap: 6px; }
  .contact-line svg { position: static; width: 11px; height: 11px; }
</style>
</head>
<body>

<section class="card card-front" aria-label="Card front">
  <svg viewBox="0 0 570 326" width="570" height="326" aria-hidden="true">
    <defs>
      <linearGradient id="goldBarFront" x1="0" y1="0" x2="0" y2="1">
        <stop offset="0" stop-color="var(--gold-deep)"/>
        <stop offset=".55" stop-color="var(--gold)"/>
        <stop offset=".56" stop-color="var(--gold-light)"/>
        <stop offset="1" stop-color="var(--gold-deep)"/>
      </linearGradient>
    </defs>
    <rect class="accent-bar" x="528" y="0" width="14" height="86" fill="url(#goldBarFront)"/>
    <rect class="accent-bar" x="30" y="240" width="14" height="86" fill="url(#goldBarFront)"/>
  </svg>
  <div class="brand-name">Gilded<br>Vantages</div>
</section>

<section class="card card-back" aria-label="Card back">
  <svg viewBox="0 0 570 326" width="570" height="326">
    <defs>
      <linearGradient id="photoTone" x1="0" y1="0" x2="0" y2="1">
        <stop offset="0" stop-color="var(--photo-sky)"/>
        <stop offset=".45" stop-color="var(--photo-house)"/>
        <stop offset="1" stop-color="var(--photo-green)"/>
      </linearGradient>
      <linearGradient id="goldSweep" x1="0" y1="0" x2="1" y2="0">
        <stop offset="0" stop-color="var(--gold-deep)"/>
        <stop offset=".5" stop-color="var(--gold-light)"/>
        <stop offset="1" stop-color="var(--gold)"/>
      </linearGradient>
    </defs>
    <polygon class="photo-area" role="img" aria-label="Photo of a home with a screened porch fitted with exterior shades"
             points="52,0 316,0 316,326 0,326" fill="url(#photoTone)"/>
    <polygon class="gold-edge" points="48,0 54,0 4,326 0,326 0,300" fill="var(--gold)"/>
    <polygon class="gold-base" points="0,326 316,326 316,268 0,306" fill="url(#goldSweep)"/>
    <rect class="gold-divider" x="316" y="0" width="5" height="326" fill="var(--gold)"/>
    <rect class="name-band-bg" x="321" y="106" width="249" height="62" fill="url(#goldSweep)"/>
  </svg>

  <div class="brand-name">Gilded<br>Vantages</div>

  <div class="name-band">
    <div class="person-name">Daniel Forsythe</div>
    <div class="person-role">Owner</div>
  </div>

  <p class="tagline">Custom Interior &amp; Exterior<br>Window Treatments</p>

  <div class="contact">
    <div class="contact-line">919-482-7034
      <svg viewBox="0 0 12 12" aria-hidden="true"><path d="M2 1h2.5l1 3-1.5 1a7 7 0 0 0 3 3l1-1.5 3 1V11A9 9 0 0 1 1 2z" fill="var(--gold)"/></svg>
    </div>
    <div class="contact-line">gildedvantages.com
      <svg viewBox="0 0 12 12" aria-hidden="true"><circle cx="6" cy="6" r="5" fill="none" stroke="var(--gold)" stroke-width="1.4"/><path d="M1 6h10M6 1c2.5 3 2.5 7 0 10M6 1c-2.5 3-2.5 7 0 10" fill="none" stroke="var(--gold)" stroke-width="1"/></svg>
    </div>
  </div>
</section>

</body>
</html>
```